Non Profit Company Looking For New Website

The website for Corvale Paddock Rehoming Society should offer the viewer beautiful photos that inspire condifence and joy and tap into our love of horses.

We would like to see a website that displays trust, quality and confidence. Needs to be responsive and mobile friendly for all browsers and coded for both Android & IOS.

READ ATTACHED WEBSITE TEMPLATE FOR COMPLETE DETAILS ON WHAT WE ARE LOOKING FOR.

Looking for recommmendations if we should use WordPress/WooCommerce for site or Wordpress with Shopify Plug in or just Shopify.

Must be both desktop and mobile friendly with fast page load speed. Need the ability to edit ourselves.

Industry/Entity Type

Non Profit

Coding

Coded - Design and coding required

Number of Pages Required

5+ page

Requirements
Must have
• We would like to see a website that displays trust, quality and confidence. Needs to be responsive and mobile friendly for all browsers and coded for both Android & IOS.

Looking for recommendations if we should use WordPress/WooCommerce for site or Wordpress with Shopify Plug in or just Shopify.

Logo Colour:
Pantone 7621 C

READ TEMPLATE THAT IS ATTACHED
Nice to have
• Like look of this website as a sample:
https://www.quillmanegallop.com/

Another similar non profit organization
https://brindlefieldrest.com/

```html
<!DOCTYPE html>
<html lang="en">
<head>
<meta charset="utf-8">
<title>Corvale Paddock Rehoming Society</title>
<link rel="stylesheet" href="https://fonts.googleapis.com/css2?family=Cinzel:wght@400;600&family=Lato:wght@400;700&display=swap">
<style>
:root{
  --red:#c01a2c;
  --red-dark:#a8121f;
  --ink:#1d1d1d;
  --body:#444;
  --muted:#8a8a8a;
  --line:#d6d6d6;
  --grey-bg:#f4f4f4;
  --white:#fff;
}
*{box-sizing:border-box;margin:0;padding:0}
html,body{width:1200px;height:3795px;overflow:hidden;background:var(--white)}
body{position:relative;font-family:"Lato",Arial,sans-serif;color:var(--body)}
.abs{position:absolute}
.serif{font-family:"Cinzel",Georgia,serif}
.btn{position:absolute;background:var(--red);color:var(--white);border-radius:24px;font-family:"Cinzel",Georgia,serif;font-size:15px;font-weight:600;display:flex;align-items:center;justify-content:center;letter-spacing:.3px}

/* header */
.topbar{left:0;top:0;width:1200px;height:52px;background:var(--white)}
.phone{left:115px;top:12px;display:flex;align-items:center;gap:12px;font-size:13px;color:#555}
.ring{width:28px;height:28px;border:2px solid var(--red);border-radius:50%;display:flex;align-items:center;justify-content:center}
.socials{left:895px;top:9px;display:flex;gap:12px}
.socials .ring{width:30px;height:30px}
.socials .dot{width:8px;height:8px;background:var(--red);border-radius:50%}
.nav{left:0;top:52px;width:1200px;height:47px;background:var(--red)}
.nav a{position:absolute;top:15px;color:var(--white);font-size:13px;text-decoration:none;letter-spacing:.4px;transform:translateX(-50%)}
.logo-disc{left:507px;top:-40px;width:180px;height:180px;border-radius:50%;background:var(--white);display:flex;flex-direction:column;align-items:center;justify-content:flex-end;padding-bottom:38px}
.logo-disc .name{font-family:"Cinzel",Georgia,serif;color:var(--red);font-size:17px;line-height:1.1}
.logo-disc .sub{font-family:"Cinzel",Georgia,serif;color:var(--red);font-size:10px;line-height:1.3;text-align:center}

/* hero */
.hero-photo{left:0;top:99px;width:1200px;height:660px;
  background:
    radial-gradient(ellipse 170px 300px at 860px 330px,rgba(92,42,22,.95),rgba(92,42,22,0) 100%),
    radial-gradient(ellipse 150px 220px at 590px 380px,rgba(38,26,22,.85),rgba(38,26,22,0) 100%),
    radial-gradient(ellipse 360px 60px at 620px 40px,rgba(236,232,224,.8),rgba(236,232,224,0) 100%),
    linear-gradient(180deg,#b7b4a4 0%,#7f8c5e 14%,#5e7f36 30%,#6d8f3c 55%,#557f2c 100%)}
.hero-shade{left:0;top:99px;width:640px;height:460px;background:linear-gradient(90deg,rgba(0,0,0,.25),rgba(0,0,0,0))}
.hero-title{left:111px;top:292px;color:var(--white);font-size:40px;line-height:46px;letter-spacing:1px}
.hero-sub{left:111px;top:450px;color:var(--white);font-size:17px;line-height:27px;width:380px}
.feature{position:absolute;width:260px;height:260px;border-radius:50%;border:7px solid var(--white);overflow:hidden;box-shadow:0 2px 6px rgba(0,0,0,.15)}
.feature .shot{width:100%;height:100%}
.feature .band{position:absolute;left:0;bottom:0;width:100%;height:66px;background:var(--red);color:var(--white);font-family:"Cinzel",Georgia,serif;font-size:20px;text-align:center;padding-top:16px;letter-spacing:1px}
.note{left:0;top:955px;width:1200px;text-align:center;font-size:17px;color:#444}

/* about */
.about-h{left:113px;top:1098px;font-size:29px;line-height:46px;color:var(--ink);letter-spacing:.5px}
.about-p{left:113px;font-size:12px;line-height:26px;width:485px;color:#444}

/* horses */
.horses{left:0;top:1556px;width:1200px;height:718px;background:var(--grey-bg)}
.sec-h{font-size:29px;color:var(--ink);letter-spacing:.5px}
.card{position:absolute;top:1697px;width:310px;height:416px;background:var(--white);box-shadow:0 1px 4px rgba(0,0,0,.08)}
.card .shot{width:100%;height:225px}
.card .fee{position:absolute;left:-4px;top:190px;background:var(--red);color:var(--white);font-family:"Cinzel",Georgia,serif;font-size:13px;padding:5px 7px}
.card .hname{position:absolute;left:19px;top:255px;font-family:"Cinzel",Georgia,serif;color:var(--red);font-size:20px}
.card .promo{position:absolute;left:20px;top:285px;font-size:12.5px;color:#444}
.card table{position:absolute;left:20px;top:302px;width:270px;border-collapse:collapse;font-size:12.5px;color:#555}
.card td{height:23px;border-bottom:1px solid #eee}
.card td.v{text-align:right;padding-right:8px;border-right:1px solid #e3e3e3}
.card td.k2{padding-left:8px}
.card td.r{text-align:right}

/* adopt */
.adopt-photo{left:0;top:2274px;width:1200px;height:420px;
  background:
    radial-gradient(ellipse 230px 130px at 300px 190px,rgba(120,72,28,.95),rgba(120,72,28,0) 100%),
    radial-gradient(ellipse 60px 30px at 1000px 225px,rgba(60,50,40,.7),rgba(60,50,40,0) 100%),
    linear-gradient(180deg,#7f96ad 0%,#a6b2ad 22%,#8a9a72 34%,#5f7c35 48%,#4b6d27 100%)}
.adopt-h{left:715px;top:2400px;color:var(--white);font-size:29px;letter-spacing:1px}
.adopt-p{left:714px;top:2456px;color:var(--white);font-size:12.5px;line-height:26px;width:380px}

/* contact */
.c-item{left:112px;display:flex;gap:16px}
.c-item .ring{width:34px;height:34px;flex:none}
.c-item .lbl{font-family:"Cinzel",Georgia,serif;color:var(--red);font-size:14px;margin-bottom:6px}
.c-item .val{font-size:13px;line-height:22px;color:#444}
.field{position:absolute;border:2px solid var(--line);border-radius:4px;font-size:12.5px;color:#aaa;padding:12px 20px}
.check{left:417px;top:3149px;width:359px;height:88px;border:1px solid #ddd;background:#f9f9f9;box-shadow:0 1px 3px rgba(0,0,0,.1)}

/* footer */
.footer{left:0;top:3371px;width:1200px;height:424px;
  background:
    radial-gradient(ellipse 300px 90px at 900px 90px,rgba(90,130,50,.55),rgba(90,130,50,0) 100%),
    radial-gradient(ellipse 260px 80px at 200px 110px,rgba(80,120,45,.5),rgba(80,120,45,0) 100%),
    linear-gradient(180deg,#ffffff 0%,#c7d8a9 18%,#5d8a2f 45%,#3f6c1f 75%,#355c1a 100%)}
.f-logo{left:113px;top:3490px;width:205px;text-align:center;color:var(--white);font-family:"Cinzel",Georgia,serif}
.f-h{color:var(--white);font-family:"Cinzel",Georgia,serif;font-size:19px;letter-spacing:.5px}
.f-list{color:var(--white);font-size:13px;line-height:26.5px;list-style:none}
.f-row{display:flex;align-items:flex-start;gap:12px;color:var(--white);font-size:13px;line-height:20px}
.f-ring{width:19px;height:19px;border:1.5px solid var(--white);border-radius:50%;flex:none;display:flex;align-items:center;justify-content:center}
.f-ring i{width:5px;height:5px;background:var(--white);border-radius:50%}
.f-rule{left:113px;top:3743px;width:975px;height:1px;background:rgba(255,255,255,.5)}
.f-copy{top:3758px;color:var(--white);font-size:13px}
</style>
</head>
<body>

<!-- header -->
<div class="abs topbar"></div>
<div class="abs phone">
  <span class="ring"><svg width="14" height="14" viewBox="0 0 24 24"><path d="M6.6 10.8a15 15 0 0 0 6.6 6.6l2.2-2.2a1 1 0 0 1 1-.25 11.4 11.4 0 0 0 3.6.57 1 1 0 0 1 1 1V20a1 1 0 0 1-1 1A17 17 0 0 1 3 4a1 1 0 0 1 1-1h3.5a1 1 0 0 1 1 1c0 1.25.2 2.45.57 3.57a1 1 0 0 1-.25 1z" fill="#c01a2c"/></svg></span>
  Phone: 012-555-0148
</div>
<div class="abs socials">
  <span class="ring"><span class="dot"></span></span>
  <span class="ring"><span class="dot"></span></span>
  <span class="ring"><span class="dot"></span></span>
  <span class="ring"><span class="dot"></span></span>
  <span class="ring"><span class="dot"></span></span>
</div>
<nav class="abs nav">
  <a style="left:175px">HOME</a>
  <a style="left:292px">ABOUT</a>
  <a style="left:408px">ADOPT</a>
  <a style="left:736px">HORSE</a>
  <a style="left:878px">DONATE/SHOP</a>
  <a style="left:1030px">CONTACT</a>
</nav>

<!-- hero -->
<div class="abs hero-photo" role="img" aria-label="Two thoroughbred horses grazing in a green paddock with a white fence and farmhouse behind"></div>
<div class="abs hero-shade"></div>
<div class="abs logo-disc">
  <div class="name">CORVALE</div>
  <div class="sub">PADDOCK<br>REHOMING</div>
</div>
<div class="abs serif hero-title">CORVALE<br>PADDOCK<br>REHOMING</div>
<div class="abs hero-sub">We support and develop retired thoroughbred racehorses for their next chapter in life.</div>

<svg class="abs" style="left:0;top:640px" width="1200" height="260" viewBox="0 0 1200 260">
  <path d="M0 75 C180 150 330 135 470 70 C600 20 720 15 820 30 C960 45 1080 55 1200 130 L1200 260 L0 260 Z" fill="#c01a2c"/>
  <path d="M0 90 C180 170 330 155 470 90 C600 40 720 38 820 50 C960 65 1080 80 1200 150 L1200 260 L0 260 Z" fill="#ffffff"/>
</svg>

<div class="feature" style="left:157px;top:650px">
  <div class="shot" role="img" aria-label="Chestnut horse with a white blaze in profile" style="background:radial-gradient(ellipse 110px 140px at 150px 140px,#c06a2a,rgba(192,106,42,0) 100%),linear-gradient(160deg,#7da04a,#a9662e 55%,#8b4a1f)"></div>
  <div class="band">RETIRED</div>
</div>
<div class="feature" style="left:465px;top:613px">
  <div class="shot" role="img" aria-label="Trainer leading a dark horse in a sand arena" style="background:radial-gradient(ellipse 50px 70px at 80px 120px,rgba(30,30,35,.85),rgba(30,30,35,0) 100%),linear-gradient(180deg,#a9c6e2 0%,#cfd9e0 35%,#8f8374 50%,#6e665c 58%,#c9b89a 75%,#b9a687 100%)"></div>
  <div class="band">RETRAIN</div>
</div>
<div class="feature" style="left:771px;top:650px">
  <div class="shot" role="img" aria-label="Young woman smiling beside a bay horse at sunset" style="background:radial-gradient(ellipse 80px 130px at 180px 140px,#7a5236,rgba(122,82,54,0) 100%),linear-gradient(150deg,#f0e4c6,#c9a97a 40%,#6e5040 70%,#2e2420)"></div>
  <div class="band">REHOME</div>
</div>

<p class="abs note">Corvale Paddock Rehoming Society (CPR) is a registered not-for-profit organization in Alberta.</p>

<!-- about -->
<h2 class="abs serif about-h" style="font-weight:400">WHAT IS<br>THOROUGHBRED AFTERCARE?</h2>
<p class="abs about-p" style="top:1220px">The health, safety and welfare of our equine athletes does not end at the finish line, and retirement and aftercare are critical to the success of the racing industry.</p>
<p class="abs about-p" style="top:1299px">Aftercare is the safe placement of racehorses after their careers as racehorse are completed. Some horses might retire to the breeding shed or broodmare bands, while others are retrained for second careers.</p>
<div class="btn" style="left:113px;top:1420px;width:148px;height:46px">LEARN MORE</div>

<svg class="abs" style="left:600px;top:1030px" width="500" height="450" viewBox="600 1030 500 450" role="img" aria-label="Woman with a long ponytail leaning against a white horse in an autumn field">
  <defs>
    <linearGradient id="tri" x1="0" y1="0" x2="0" y2="1"><stop offset="0" stop-color="#e4dccf"/><stop offset=".45" stop-color="#c79a72"/><stop offset=".75" stop-color="#a4663e"/><stop offset="1" stop-color="#7a4a2c"/></linearGradient>
    <radialGradient id="glow" cx=".45" cy=".55" r=".35"><stop offset="0" stop-color="#f3f0ea" stop-opacity=".85"/><stop offset="1" stop-color="#f3f0ea" stop-opacity="0"/></radialGradient>
  </defs>
  <polygon points="843,1062 632,1458 1054,1458" fill="url(#tri)"/>
  <polygon points="843,1062 632,1458 1054,1458" fill="url(#glow)"/>
  <polygon points="843,1039 806,1108 880,1108" fill="#c01a2c"/>
  <polygon points="611,1466 645,1384 690,1466" fill="#c01a2c"/>
  <polygon points="1085,1466 1041,1384 996,1466" fill="#c01a2c"/>
</svg>

<!-- horses -->
<div class="abs horses"></div>
<h2 class="abs serif sec-h" style="left:0;top:1615px;width:1200px;text-align:center;font-weight:400">OUR HORSES</h2>
<div class="btn" style="left:888px;top:1612px;width:198px;height:46px;font-size:14px">MORE WAYS TO GIVE</div>

<svg class="abs" style="left:40px;top:1908px" width="34" height="26" viewBox="0 0 34 26"><path d="M33 13H3M14 2L3 13l11 11" stroke="#aaa" stroke-width="2" fill="none"/></svg>
<svg class="abs" style="left:1130px;top:1908px" width="34" height="26" viewBox="0 0 34 26"><path d="M1 13h30M20 2l11 11-11 11" stroke="#aaa" stroke-width="2" fill="none"/></svg>

<div class="card" style="left:113px">
  <div class="shot" role="img" aria-label="Bay horse standing by a white fence in autumn" style="background:radial-gradient(ellipse 80px 60px at 140px 120px,rgba(110,40,20,.9),rgba(110,40,20,0) 100%),linear-gradient(180deg,#6e7f34,#a57a3a 35%,#d6d6cf 52%,#6f8c3e 62%,#5d7a33)"></div>
  <div class="fee">FEE: $1,000</div>
  <div class="hname">HORSE NAME</div>
  <div class="promo">NOW $800 UNTIL 5/31</div>
  <table><tr><td>Height</td><td class="v">15.2</td><td class="k2">Birth Year</td><td class="r">2016</td></tr>
  <tr><td>Color</td><td class="v">Bay</td><td class="k2">Gender</td><td class="r">Mare</td></tr>
  <tr><td>Location</td><td colspan="3" class="r">ASHBY CREEK, OH</td></tr></table>
</div>
<div class="card" style="left:445px">
  <div class="shot" role="img" aria-label="Brown horse on an open grass field under a cloudy sky" style="background:radial-gradient(ellipse 80px 50px at 140px 120px,rgba(120,66,34,.9),rgba(120,66,34,0) 100%),linear-gradient(180deg,#b9cbe0,#e7ecef 40%,#7aa24a 55%,#5e8c35)"></div>
  <div class="fee">FEE: $1,000</div>
  <div class="hname">HORSE NAME</div>
  <div class="promo">NOW $800 UNTIL 5/31</div>
  <table><tr><td>Height</td><td class="v">16.1</td><td class="k2">Birth Year</td><td class="r">2007</td></tr>
  <tr><td>Color</td><td class="v">Bay</td><td class="k2">Gender</td><td class="r">Gelding</td></tr>
  <tr><td>Location</td><td colspan="3" class="r">WREN FALLS, NY</td></tr></table>
</div>
<div class="card" style="left:777px">
  <div class="shot" role="img" aria-label="White horse in a forest clearing at golden hour" style="background:radial-gradient(ellipse 70px 60px at 125px 110px,rgba(240,238,232,.9),rgba(240,238,232,0) 100%),linear-gradient(180deg,#2f4a2a,#6b5a2e 45%,#b98a3e 72%,#6d5a2a)"></div>
  <div class="fee">FEE: $1,000</div>
  <div class="hname">HORSE NAME</div>
  <div class="promo">NOW $800 UNTIL 5/31</div>
  <table><tr><td>Height</td><td class="v">15.3</td><td class="k2">Birth Year</td><td class="r">2016</td></tr>
  <tr><td>Color</td><td class="v">Bay</td><td class="k2">Gender</td><td class="r">Mare</td></tr>
  <tr><td>Location</td><td colspan="3" class="r">TALLOW RIDGE, KY</td></tr></table>
</div>
<div class="btn" style="left:509px;top:2164px;width:177px;height:46px;font-size:14px">VIEW ALL HORSES</div>

<!-- adopt -->
<div class="abs adopt-photo" role="img" aria-label="Bay horse grazing in a wide meadow with an old wagon in the distance"></div>
<h2 class="abs serif adopt-h" style="font-weight:400">ADOPT A HORSE</h2>
<p class="abs adopt-p">Corvale Paddock Rehoming is committed to helping match you with the perfect horse.</p>
<div class="btn" style="left:714px;top:2529px;width:147px;height:46px;font-size:14px">ADOPT NOW</div>

<!-- contact -->
<h2 class="abs serif sec-h" style="left:0;top:2775px;width:1200px;text-align:center;font-weight:400">HAVE A QUESTION OR NEED MORE INFORMATION?</h2>

<div class="abs c-item" style="top:2893px">
  <span class="ring"><svg width="14" height="16" viewBox="0 0 24 28"><path d="M12 1a9 9 0 0 0-9 9c0 7 9 17 9 17s9-10 9-17a9 9 0 0 0-9-9zm0 12a3 3 0 1 1 0-6 3 3 0 0 1 0 6z" fill="#c01a2c"/></svg></span>
  <div><div class="lbl">LOCATION</div><div class="val">4127 Fernhollow Lane<br>Marlowe, MD 21990</div></div>
</div>
<div class="abs c-item" style="top:2976px">
  <span class="ring"><svg width="14" height="14" viewBox="0 0 24 24"><path d="M6.6 10.8a15 15 0 0 0 6.6 6.6l2.2-2.2a1 1 0 0 1 1-.25 11.4 11.4 0 0 0 3.6.57 1 1 0 0 1 1 1V20a1 1 0 0 1-1 1A17 17 0 0 1 3 4a1 1 0 0 1 1-1h3.5a1 1 0 0 1 1 1c0 1.25.2 2.45.57 3.57a1 1 0 0 1-.25 1z" fill="#c01a2c"/></svg></span>
  <div><div class="lbl">CALL US</div><div class="val">012-555-0148</div></div>
</div>
<div class="abs c-item" style="top:3053px">
  <span class="ring"><svg width="14" height="12" viewBox="0 0 24 18"><rect x="1" y="1" width="22" height="16" rx="2" fill="#c01a2c"/><path d="M2 3l10 7 10-7" stroke="#fff" stroke-width="2" fill="none"/></svg></span>
  <div><div class="lbl">MAIL US</div><div class="val">info@corvalepaddock.org</div></div>
</div>

<div class="field" style="left:417px;top:2897px;width:323px;height:41px">First Name</div>
<div class="field" style="left:761px;top:2897px;width:325px;height:41px">Last Name</div>
<div class="field" style="left:417px;top:2953px;width:323px;height:41px">Phone#</div>
<div class="field" style="left:761px;top:2953px;width:325px;height:41px">Email Address</div>
<div class="field" style="left:417px;top:3016px;width:669px;height:112px">How can we help you?</div>

<div class="abs check">
  <div class="abs" style="left:15px;top:29px;width:30px;height:30px;border:2px solid #c1c1c1;border-radius:3px;background:#fff"></div>
  <div class="abs" style="left:62px;top:35px;font-size:15px;color:#333;font-family:Arial,sans-serif">I'm not a robot</div>
  <div class="abs" style="left:296px;top:20px;width:28px;height:28px;background:#c9d3e6;border-radius:4px"></div>
  <div class="abs" style="left:296px;top:54px;font-size:10px;color:#666;font-family:Arial,sans-serif">Verify</div>
</div>

<div class="btn" style="left:415px;top:3262px;width:153px;height:44px;gap:12px">SUBMIT
  <svg width="22" height="18" viewBox="0 0 24 20"><path d="M1 9L23 1 17 19l-5-6-4 4v-6l12-8-14 7z" fill="#fff"/></svg>
</div>

<!-- footer -->
<div class="abs footer" role="img" aria-label="Close-up of tall green grass meadow"></div>
<div class="abs f-logo">
  <div style="font-size:32px;line-height:40px">CORVALE</div>
  <div style="width:70px;height:70px;border-radius:50%;border:2px solid #fff;margin:22px auto 24px"></div>
  <div style="font-size:21px;line-height:26px">PADDOCK<br>REHOMING</div>
</div>

<div class="abs f-h" style="left:422px;top:3503px">QUICK LINKS</div>
<ul class="abs f-list" style="left:424px;top:3558px">
  <li>Home</li><li>About</li><li>Adopt</li><li>Horse</li><li>Donate/Shop</li><li>Contact</li>
</ul>

<div class="abs f-h" style="left:624px;top:3503px">CONTACT INFO.</div>
<div class="abs f-row" style="left:626px;top:3564px"><span class="f-ring"><i></i></span><span>4127 Fernhollow Lane<br>Marlowe, MD 21990</span></div>
<div class="abs f-row" style="left:622px;top:3617px"><span class="f-ring"><i></i></span><span>012-555-0148</span></div>
<div class="abs f-row" style="left:622px;top:3667px"><span class="f-ring"><i></i></span><span>info@corvalepaddock.org</span></div>

<div class="abs f-h" style="left:892px;top:3501px">CONNECT WITH US</div>
<div class="abs" style="left:896px;top:3560px;display:flex;flex-direction:column;gap:6.5px">
  <div class="f-row"><span class="f-ring"><i></i></span><span>Community</span></div>
  <div class="f-row"><span class="f-ring"><i></i></span><span>Updates</span></div>
  <div class="f-row"><span class="f-ring"><i></i></span><span>Mail</span></div>
  <div class="f-row"><span class="f-ring"><i></i></span><span>Photos</span></div>
  <div class="f-row"><span class="f-ring"><i></i></span><span>Videos</span></div>
</div>

<div class="abs f-rule"></div>
<div class="abs f-copy" style="left:113px">© Copyright 2021 Corvale Paddock Rehoming - All rights reserved.</div>
<div class="abs f-copy" style="left:855px">Privacy policy &nbsp;-&nbsp; Terms &amp; conditions</div>

</body>
</html>
```